Cover for book on creating escape rooms for educational purposes

A small business (cipher vault academy) needs a book cover design for a new book they are launching as a how-to guide to create educational escape rooms. The target audience is for educators wanting to better engage their students of all ages (Primary, Secondary, Tertiary, Corporate Training).
Book Title: Boundless Classrooms
Sub Title: Harnessing the thrill of puzzle games to make teaching memorable
Authors: Dr Martin and Helen Blake

Book is to be sold on Brindlecart books as a Pagelume eBook and hard copy

Target Market(s)

Educators/Teachers

Industry/Entity Type

Education

Requirements
Must have
• Cipher Vault Academy Logo
Should not have
• A focus only on children

```html
<!DOCTYPE html>
<html lang="en">
<head>
<meta charset="utf-8">
<title>Boundless Classrooms — Book Cover</title>
<link href="https://fonts.googleapis.com/css2?family=Anton&family=Mulish:wght@500;700&display=swap" rel="stylesheet">
<style>
  :root {
    --stage: #e9e6dc;
    --cover-light: #eef5c4;
    --cover-mid: #b9dc92;
    --cover-deep: #4f9a4e;
    --ink-green: #0d3f2c;
    --maze-green: #2fbf3f;
    --maze-dark: #0f3a1a;
    --accent-orange: #f07c1e;
    --paper: #ffffff;
  }
  * { margin: 0; padding: 0; box-sizing: border-box; }
  html, body { width: 1200px; height: 906px; overflow: hidden; }
  body {
    background: var(--stage);
    display: flex;
    align-items: center;
    justify-content: center;
    font-family: "Mulish", "Trebuchet MS", sans-serif;
  }
  .book-cover {
    position: relative;
    width: 560px;
    height: 840px;
    overflow: hidden;
    background:
      linear-gradient(150deg, var(--cover-light) 0%, var(--cover-mid) 45%, var(--cover-deep) 100%);
  }
  .authors {
    position: absolute;
    top: 62px;
    left: 0;
    width: 100%;
    text-align: center;
    font-size: 30px;
    font-weight: 500;
    color: var(--ink-green);
    letter-spacing: 0.2px;
  }
  .cover-art {
    position: absolute;
    top: 160px;
    left: 100px;
    width: 370px;
    height: 360px;
    border-radius: 10px;
    background: radial-gradient(circle at 55% 50%, var(--maze-green) 0%, #1f8c2c 55%, var(--maze-dark) 100%);
  }
  .title {
    position: absolute;
    top: 520px;
    left: 50px;
    width: 460px;
    font-family: "Anton", "Impact", sans-serif;
    color: var(--ink-green);
    text-transform: uppercase;
    line-height: 0.95;
  }
  .title-line { display: block; }
  .title-line--first { font-size: 74px; letter-spacing: 1px; }
  .title-line--second { font-size: 84px; letter-spacing: 0.5px; }
  .subtitle {
    position: absolute;
    top: 720px;
    left: 20px;
    width: 520px;
    text-align: center;
    font-size: 19px;
    font-weight: 500;
    line-height: 1.25;
    color: #111;
    z-index: 2;
  }
  .footer-curve {
    position: absolute;
    left: 0;
    bottom: 0;
    width: 560px;
    height: 140px;
  }
  .publisher {
    position: absolute;
    left: 28px;
    bottom: 30px;
    display: flex;
    align-items: center;
    gap: 8px;
    z-index: 2;
  }
  .publisher-dot {
    width: 18px;
    height: 18px;
    border-radius: 50%;
    background: var(--accent-orange);
  }
  .publisher-name {
    font-size: 14px;
    font-weight: 700;
    color: var(--accent-orange);
    text-transform: uppercase;
    letter-spacing: 0.5px;
  }
</style>
</head>
<body>
  <main class="book-cover">
    <p class="authors">Dr Martin and Helen Blake</p>

    <div class="cover-art" role="img" aria-label="Illustration of a green 3D maze cube with a golden key inserted in its side"></div>

    <h1 class="title">
      <span class="title-line title-line--first">Boundless</span>
      <span class="title-line title-line--second">Classrooms</span>
    </h1>

    <svg class="footer-curve" viewBox="0 0 560 140" preserveAspectRatio="none" aria-hidden="true">
      <path d="M0 30 C 90 10, 200 40, 300 140 L 0 140 Z" fill="var(--paper)"/>
    </svg>

    <p class="subtitle">Harnessing the thrill of puzzle games<br>to make teaching memorable</p>

    <div class="publisher">
      <span class="publisher-dot"></span>
      <span class="publisher-name">Cipher Vault Academy</span>
    </div>
  </main>
</body>
</html>
```